Organic Infographic – "The 4 Dimensions of Transformation"

Overview:
We are a coaching/education brand (Brightmoor Institute) and need a redesigned infographic illustrating our 4-area transformation model. Our current version (attached) uses a rigid, hard-edged triangle/pyramid layout — we want a completely new visual approach that feels organic, soft, and alive, since the topic is human personal development, not a technical process.

Content structure (please keep the wording, redesign the visual form):

4 areas: "Embodiment – The Foundation" and "Focus & Intuition Redefined – The Lens" sit on the same base level. "Heart Centered Living – The Bridge" sits one level above, connecting/enabling the other two. "Becoming Unlimited – The Peak" sits at the top, made possible by Heart Centered Living.
The 4 areas influence and inspire one another — this mutual connection must be visually recognizable (e.g. through overlapping zones, blended color transitions, connecting flowing lines, or similar). Areas may stay visually distinct; the connection between them is what must be shown.
Hierarchy should be expressed mainly through position/arrangement (ascending flow), not through size differences — all 4 areas should carry similar visual weight, since each is equally essential.
A supporting element: "The Brightmoor Methodology" with 3 phases (Phase 1: Awareness & Insight, Phase 2: Integration & Practice, Phase 3: Expansion & Sustainable Growth), each with a short description (text provided below).

Style direction:
Organic, soft, flowing shapes — no sharp angles or rigid geometric triangles. Attached are 3 moodboard references showing the direction we like: overlapping/blended circular shapes, flowing ribbon-style connections, and organic swirl divisions. Please don't copy any of them directly — combine this organic/overlapping visual language with our specific asymmetric hierarchy (2 areas base level + 1 bridge + 1 peak), which none of the references show exactly. This creative translation is the core task.

Icons: Please design one new, unified icon per area (4 total) plus 3 simple icons for the methodology phases — consistent style across all 7, your creative interpretation is welcome.

Typography: Headlines in Arsenal, body text in DM Sans.

Colors: Base palette — Embodiment D09176, Focus & Intuition Redefined B6623E, Heart Centered Living D9866B, Becoming Unlimited 6F7A70, dark text 23211A, light accent EACEC1. Slight adjustments are welcome if they improve visual distinction between areas.

Technical requirements (important):

Final files as vector format (SVG, AI, or EPS), with separated, editable, non-flattened/non-merged layers and paths.
Shapes should consist of simple, closed outline paths — no fine textures, no complex multi-stop gradients, no photorealistic rendering — since the artwork will later be manually redrawn as a whiteboard-animation video.
Primary format: 16:9 landscape. A secondary vertical/mobile version (3 outer areas stacked below the top area) is welcome but optional.

Usage rights: Full commercial usage across website, video, and social media required.

Attachments to include: current draft PDF (for text content and logo reference only — not for layout), our logo file, and the 3 moodboard reference images.

Budget: $100–150 — please let us know if this realistically allows for more designer participation, or advise on adjusting scope/budget

Methodology phase texts (for the 3 supporting icons):

Phase 1: Awareness & Insight
Cultivating self-reflection, identifying patterns, and gaining clarity on personal drivers through introspective practices and data-informed assessment.

Phase 2: Integration & Practice
Applying tools and frameworks, developing new habits, and aligning actions with core values through consistent application and feedback loops.

Phase 3: Expansion & Sustainable Growth
Achieving long-term transformation, exceeding limitations, and fostering resilience through continuous evolution and a purpose-driven approach.

```html
<!DOCTYPE html>
<html lang="en">
<head>
<meta charset="utf-8">
<title>The 4 Dimensions of Transformation – Brightmoor Institute</title>
<link rel="stylesheet" href="https://fonts.googleapis.com/css2?family=DM+Sans:wght@400;500&family=Lato:wght@400&family=Marcellus&family=Montserrat:wght@400;600&display=swap">
<style>
  :root {
    --stage: #383838;
    --card-top: #ffffff;
    --card-bottom: #f5e2d8;
    --embodiment: #d09176;
    --focus: #b6623e;
    --heart: #d9866b;
    --unlimited: #6f7a70;
    --dark: #23211a;
    --title-dark: #2c2c2c;
    --accent: #eacec1;
    --rust: #b35e3c;
    --rust-deep: #a0532f;
    --icon: #7a3e22;
    --brand-grey: #8a978c;
    --light-text: #fbefe8;
  }
  html, body {
    margin: 0;
    width: 1200px;
    height: 1200px;
    overflow: hidden;
    background: var(--stage);
  }
  .canvas { display: block; width: 1200px; height: 1200px; }
  .title { font-family: "Montserrat", sans-serif; font-weight: 600; }
  .title-accent { fill: var(--rust); }
  .title-sub { fill: var(--title-dark); letter-spacing: 4px; }
  .brand-name { font-family: "Montserrat", sans-serif; font-weight: 400; fill: var(--brand-grey); }
  .method-title { font-family: "Montserrat", sans-serif; font-weight: 400; fill: var(--rust-deep); }
  .phase-heading { font-family: "DM Sans", sans-serif; font-weight: 400; fill: var(--rust); font-size: 22px; }
  .phase-body { font-family: "DM Sans", sans-serif; fill: var(--dark); font-size: 16.5px; }
  .area-heading { font-family: "Marcellus", serif; fill: var(--dark); }
  .area-sub { font-family: "Marcellus", serif; fill: var(--light-text); }
  .area-body { font-family: "Lato", sans-serif; fill: var(--dark); font-size: 15.5px; }
  .area-body-light { fill: var(--light-text); }
  .area-ring { fill: none; stroke: var(--dark); stroke-opacity: .35; stroke-width: 1.5; }
  .phase-icon { fill: none; stroke: var(--icon); stroke-width: 3.5; stroke-linecap: round; stroke-linejoin: round; }
</style>
</head>
<body>
<svg class="canvas" viewBox="0 0 1932 1932" xmlns="http://www.w3.org/2000/svg">
  <defs>
    <linearGradient id="cardWash" x1="0.7" y1="0" x2="0.2" y2="1">
      <stop offset="0" stop-color="var(--card-top)"/>
      <stop offset="1" stop-color="var(--card-bottom)"/>
    </linearGradient>
  </defs>

  <rect class="card" x="203" y="517" width="1617" height="909" fill="url(#cardWash)"/>

  <!-- Headline -->
  <g class="headline">
    <rect x="268" y="557" width="6" height="146" fill="var(--rust)"/>
    <rect x="284" y="557" width="6" height="146" fill="var(--title-dark)"/>
    <text class="title title-accent" x="302" y="632" font-size="68">The</text>
    <text class="title title-accent" x="448" y="630" font-size="112">4</text>
    <text class="title title-accent" x="543" y="632" font-size="68">Dimensions</text>
    <text class="title title-sub" x="302" y="688" font-size="55">OF TRANSFORMATION</text>
  </g>

  <!-- Brand -->
  <g class="brand">
    <circle cx="1245" cy="605" r="58" fill="var(--embodiment)"/>
    <text class="brand-name" x="1322" y="620" font-size="40">Brightmoor Institute</text>
  </g>

  <!-- Dimensions model -->
  <g class="dimensions">
    <g class="area area-unlimited">
      <circle cx="715" cy="925" r="162" fill="none" stroke="var(--unlimited)" stroke-width="3"/>
      <path d="M561,945 A155,155 0 1 1 869,945 C800,972 640,962 561,945Z" fill="var(--unlimited)"/>
    </g>
    <g class="area area-heart">
      <path d="M460,1040 C450,960 560,925 650,935 C760,945 800,975 880,960 C950,950 985,1010 970,1070 C955,1120 880,1130 800,1110 C740,1095 690,1100 620,1115 C520,1135 468,1095 460,1040Z" fill="var(--heart)" fill-opacity=".92"/>
      <path d="M460,1040 C450,960 560,925 650,935 C760,945 800,975 880,960 C950,950 985,1010 970,1070 C955,1120 880,1130 800,1110 C740,1095 690,1100 620,1115 C520,1135 468,1095 460,1040Z" fill="none" stroke="var(--heart)" stroke-width="3" transform="translate(715 1035) scale(1.03) translate(-715 -1035)"/>
    </g>
    <g class="area area-embodiment">
      <path d="M268,1170 C260,1080 330,1045 430,1052 C540,1060 600,1090 660,1110 C700,1125 725,1160 720,1200 C640,1240 520,1260 430,1272 C320,1285 272,1240 268,1170Z" fill="var(--embodiment)" fill-opacity=".92"/>
      <path d="M268,1170 C260,1080 330,1045 430,1052 C540,1060 600,1090 660,1110 C700,1125 725,1160 720,1200 C640,1240 520,1260 430,1272 C320,1285 272,1240 268,1170Z" fill="none" stroke="var(--embodiment)" stroke-width="3" transform="translate(495 1165) scale(1.035) translate(-495 -1165)"/>
    </g>
    <g class="area area-focus">
      <path d="M695,1190 C690,1140 780,1110 850,1085 C930,1055 1020,1040 1090,1065 C1150,1090 1170,1160 1150,1215 C1130,1265 1070,1275 990,1270 C900,1265 800,1240 730,1220 C705,1212 696,1203 695,1190Z" fill="var(--focus)" fill-opacity=".95"/>
      <path d="M695,1190 C690,1140 780,1110 850,1085 C930,1055 1020,1040 1090,1065 C1150,1090 1170,1160 1150,1215 C1130,1265 1070,1275 990,1270 C900,1265 800,1240 730,1220 C705,1212 696,1203 695,1190Z" fill="none" stroke="var(--focus)" stroke-width="3" transform="translate(930 1160) scale(1.035) translate(-930 -1160)"/>
    </g>

    <circle class="area-ring" cx="714" cy="798" r="20"/>
    <circle class="area-ring" cx="574" cy="997" r="30"/>
    <circle class="area-ring" cx="398" cy="1080" r="20"/>
    <circle class="area-ring" cx="1016" cy="1095" r="32"/>

    <g class="area-text" text-anchor="middle">
      <text class="area-heading" x="712" y="846" font-size="25">Becoming Unlimited</text>
      <text class="area-sub" x="712" y="873" font-size="24">– The Peak</text>
      <text class="area-body" x="716" y="897">Lorem ipsum dolor sit amet,</text>
      <text class="area-body" x="716" y="917">consectetuer adipiscing elit.</text>

      <text class="area-heading" x="748" y="997" font-size="28">Heart Centered Living</text>
      <text class="area-sub" x="740" y="1024" font-size="27">– The Bridge</text>
    </g>
    <text class="area-body" x="575" y="1050">Lorem ipsum dolor sit amet, consectetuer</text>
    <text class="area-body" x="575" y="1069">adipiscing elit, sed diam nonummy nibh.</text>

    <text class="area-heading" x="318" y="1128" font-size="29">Embodiment</text>
    <text class="area-sub" x="318" y="1158" font-size="28">– The Foundation</text>
    <text class="area-body" x="318" y="1185">Lorem ipsum dolor sit amet, consectetuer</text>
    <text class="area-body" x="318" y="1203">adipiscing elit, sed diam nonummy nibh</text>
    <text class="area-body" x="318" y="1221">euismod tincidunt adipiscing</text>

    <g text-anchor="end">
      <text class="area-heading" x="1094" y="1155" font-size="26">Focus &amp; Intuition</text>
      <text class="area-heading" x="1100" y="1182" font-size="22">Redefined <tspan class="area-sub">– The Lens</tspan></text>
      <text class="area-body area-body-light" x="1100" y="1206">Lorem ipsum dolor sit amet, consectetuer</text>
      <text class="area-body area-body-light" x="1097" y="1224">adipiscing elit, sed diam nonummy nibh</text>
      <text class="area-body area-body-light" x="1100" y="1243">euismod tincidunt adipiscing</text>
    </g>
  </g>

  <!-- Methodology -->
  <g class="methodology">
    <text class="method-title" x="1155" y="815" font-size="42" textLength="613" lengthAdjust="spacingAndGlyphs">The Brightmoor Methodology</text>

    <g class="phase phase-awareness">
      <path class="phase-icon" d="M1280,965 L1280,945 C1262,930 1262,895 1285,882 C1305,870 1335,878 1340,905 L1348,922 L1340,925 L1340,945 L1320,948 L1320,965"/>
      <circle class="phase-icon" cx="1298" cy="910" r="13"/>
      <circle class="phase-icon" cx="1298" cy="910" r="4"/>
      <text class="phase-heading" x="1370" y="900">Phase 1: Awareness &amp; Insight</text>
      <text class="phase-body" x="1370" y="923">Cultivating self-reflection, identifying patterns</text>
      <text class="phase-body" x="1370" y="944">and gaining clarity on personal drivers through</text>
      <text class="phase-body" x="1370" y="964">introspective practices and data-informed assessment.</text>
    </g>

    <g class="phase phase-integration">
      <path class="phase-icon" d="M1284,1095 C1284,1080 1268,1075 1268,1055 C1268,1035 1283,1022 1300,1022 C1317,1022 1332,1035 1332,1055 C1332,1075 1316,1080 1316,1095Z"/>
      <path class="phase-icon" d="M1286,1104 H1314 M1288,1113 H1312 M1294,1122 H1306"/>
      <path class="phase-icon" d="M1300,1068 L1288,1056 C1282,1049 1288,1040 1295,1043 L1300,1047 L1305,1043 C1312,1040 1318,1049 1312,1056Z"/>
      <text class="phase-heading" x="1368" y="1053">Phase 2: Integration &amp; Practice</text>
      <text class="phase-body" x="1368" y="1075">Applying tools and frameworks, developing new habits</text>
      <text class="phase-body" x="1368" y="1096">and aligning actions with core values through consistent</text>
      <text class="phase-body" x="1368" y="1116">application and feedback loops.</text>
    </g>

    <g class="phase phase-expansion">
      <path class="phase-icon" d="M1280,1177 H1314 A4,4 0 0 1 1318,1181 V1201 A4,4 0 0 1 1314,1205 H1292 L1284,1213 V1205 H1280 A4,4 0 0 1 1276,1201 V1181 A4,4 0 0 1 1280,1177Z M1285,1187 H1309 M1285,1195 H1302"/>
      <circle class="phase-icon" cx="1266" cy="1222" r="7"/>
      <circle class="phase-icon" cx="1296" cy="1230" r="8"/>
      <circle class="phase-icon" cx="1326" cy="1222" r="7"/>
      <path class="phase-icon" d="M1250,1248 C1250,1236 1282,1236 1282,1248 M1310,1248 C1310,1236 1342,1236 1342,1248 M1278,1260 C1278,1244 1314,1244 1314,1260"/>
      <text class="phase-heading" x="1362" y="1201">Phase 3: Expansion &amp; Sustainable Growth</text>
      <text class="phase-body" x="1362" y="1226">Achieving long-term transformation, exceeding limitations</text>
      <text class="phase-body" x="1362" y="1247">and fostering resilience through continuous evolution and</text>
      <text class="phase-body" x="1362" y="1268">a purpose-driven approach.</text>
    </g>
  </g>
</svg>
</body>
</html>
```